Veltrano - Mechanic/Collision Center Business Card

We're looking for a business card design for our mechanic/ collision repair shop.

Can be with colours or monochromatic.

See the attached files.

Many thanks

```html
<!DOCTYPE html>
<html lang="pt">
<head>
<meta charset="utf-8">
<title>Veltrano – Business Card</title>
<link href="https://fonts.googleapis.com/css2?family=Exo+2:ital,wght@0,400;0,600;1,800&display=swap" rel="stylesheet">
<style>
  :root{
    --stage:#2a2a2a;
    --card:#1c2023;
    --blue:#1e9ed9;
    --blue-light:#aed2ef;
    --white:#ffffff;
    --grey:#d9dde0;
  }
  *{margin:0;padding:0;box-sizing:border-box}
  html,body{width:1200px;height:900px;overflow:hidden}
  body{background:var(--stage);font-family:"Exo 2",sans-serif;position:relative}
  .card{position:absolute;left:250px;width:700px;height:400px;background:var(--card);overflow:hidden;box-shadow:0 10px 30px rgba(0,0,0,.5)}
  .card--front{top:40px}
  .card--back{top:460px}
  .front__bands{position:absolute;left:0;top:0;width:700px;height:400px}
  .front__mark{position:absolute;left:0;top:60px;width:700px;height:140px;display:flex;align-items:center;justify-content:center}
  .front__mark-name{font-weight:600;font-size:72px;letter-spacing:4px;color:var(--white);text-transform:uppercase}
  .holder{position:absolute;right:430px;top:88px;text-align:right}
  .holder__name{font-style:italic;font-weight:800;font-size:30px;color:var(--blue);text-transform:uppercase;letter-spacing:1px}
  .holder__role{font-size:18px;color:var(--grey);margin-top:-4px}
  .brand{position:absolute;left:300px;top:96px;display:flex;align-items:center;gap:14px}
  .brand__dot{width:30px;height:30px;border-radius:50%;background:var(--blue)}
  .brand__name{font-weight:600;font-size:48px;color:var(--white);text-transform:uppercase;letter-spacing:2px}
  .contacts{position:absolute;left:300px;top:196px;list-style:none}
  .contacts li{display:flex;align-items:center;gap:12px;font-size:19px;color:var(--white);height:25px}
  .contacts svg{width:18px;height:18px;flex:none}
  .address{position:absolute;left:290px;top:312px;font-size:20px;line-height:24px;color:var(--white)}
</style>
</head>
<body>
  <section class="card card--front">
    <svg class="front__bands" viewBox="0 0 700 400" aria-hidden="true">
      <path d="M0 210 L700 300 L700 400 L0 400 Z" fill="var(--blue)"/>
      <path d="M0 250 Q330 270 700 350 L700 400 L0 400 Z" fill="var(--blue-light)" opacity=".95"/>
      <path d="M0 250 Q330 270 700 350 L700 360 Q330 282 0 262 Z" fill="var(--blue)"/>
    </svg>
    <div class="front__mark"><span class="front__mark-name">Veltrano</span></div>
  </section>

  <section class="card card--back">
    <div class="holder">
      <div class="holder__name">Rui Matos</div>
      <div class="holder__role">Manager</div>
    </div>
    <div class="brand">
      <span class="brand__dot"></span>
      <span class="brand__name">Veltrano</span>
    </div>
    <ul class="contacts">
      <li><svg viewBox="0 0 24 24"><circle cx="12" cy="12" r="10" fill="none" stroke="var(--blue)" stroke-width="2"/><path d="M8 7l2 0 1 3-1.5 1a7 7 0 0 0 3.5 3.5l1-1.5 3 1v2a1 1 0 0 1-1 1A10 10 0 0 1 7 8a1 1 0 0 1 1-1z" fill="var(--blue)"/></svg>+351 210004127</li>
      <li><svg viewBox="0 0 24 24"><rect x="6" y="2" width="12" height="20" rx="2" fill="none" stroke="var(--blue)" stroke-width="2"/><circle cx="12" cy="18" r="1.3" fill="var(--blue)"/></svg>+351 910007356</li>
      <li><svg viewBox="0 0 24 24"><rect x="2" y="5" width="20" height="14" rx="1" fill="none" stroke="var(--blue)" stroke-width="2"/><path d="M2 6l10 7 10-7" fill="none" stroke="var(--blue)" stroke-width="2"/></svg>veltrano.office@mailbox.pt</li>
      <li><svg viewBox="0 0 24 24"><circle cx="12" cy="12" r="10" fill="var(--blue)"/></svg>www.social.pt/veltrano</li>
    </ul>
    <p class="address">Rua do Norte, 42<br>1200-286 Lisboa</p>
  </section>
</body>
</html>
```